Business Card

I need my new "Advisory" logo incorporated into my existing business card. I want the whole card redesigned. I would like to see a design with the existing colours and a few new colour options. The current card is not elegant or classy enough.

```html
<!DOCTYPE html>
<html lang="en">
<head>
<meta charset="utf-8">
<title>Business Card – Front and Back</title>
<link href="https://fonts.googleapis.com/css2?family=Montserrat:wght@500;600;700&family=Didact+Gothic&family=Alegreya+Sans:wght@500&display=swap" rel="stylesheet">
<style>
  :root {
    --ink: #191919;
    --cyan: #00bde0;
    --cyan-deep: #0a8fad;
    --paper: #ffffff;
    --text-dark: #3d3d3d;
    --text-soft: #4a4a4a;
    --stage: #eeeeee;
  }
  html, body {
    margin: 0;
    width: 1200px;
    height: 1200px;
    overflow: hidden;
    background: var(--stage);
  }
  .canvas { position: relative; width: 1200px; height: 1200px; }
  .card {
    position: absolute;
    left: 289px;
    width: 622px;
    height: 373px;
    overflow: hidden;
  }
  .card--front { top: 188px; background: var(--paper); }
  .card--back  { top: 638px; background: var(--ink); }
  .card__shapes { position: absolute; inset: 0; }

  .brand-mini {
    position: absolute; left: 57px; top: 32px; margin: 0;
    font-family: "Alegreya Sans", sans-serif; font-weight: 500;
    font-size: 14px; color: var(--paper);
  }

  .division {
    position: absolute; left: 94px; top: 188px;
  }
  .division__name {
    font-family: "Montserrat", sans-serif; font-weight: 700;
    font-size: 23px; color: var(--paper); letter-spacing: 0.5px; line-height: 1;
  }
  .division__tagline {
    font-family: "Montserrat", sans-serif; font-weight: 600;
    font-size: 10.5px; color: var(--paper); letter-spacing: 1.6px; margin-top: 6px;
  }

  .contact-icons { position: absolute; left: 0; top: 0; }

  .holder__name {
    position: absolute; left: 361px; top: 49px; margin: 0;
    font-family: "Montserrat", sans-serif; font-weight: 600;
    font-size: 23.5px; color: var(--text-dark); letter-spacing: 0.4px;
    white-space: nowrap;
  }
  .holder__name .accent { color: var(--cyan); }
  .holder__details {
    position: absolute; left: 382px; top: 149px; margin: 0; padding: 0;
    list-style: none;
    font-family: "Didact Gothic", sans-serif; font-size: 13.5px; color: var(--text-soft);
  }
  .holder__details li { height: 30px; line-height: 18px; }
  .holder__details li:nth-child(2) { height: 27px; }

  .back-brand__name {
    position: absolute; left: 187px; top: 203px; margin: 0;
    font-family: "Alegreya Sans", sans-serif; font-weight: 500;
    font-size: 36px; color: var(--paper); line-height: 1;
  }
  .back-brand__tagline {
    position: absolute; left: 187px; top: 241px; margin: 0;
    font-family: "Montserrat", sans-serif; font-weight: 600;
    font-size: 12px; color: var(--paper); letter-spacing: 0.3px;
  }
  .card__band {
    position: absolute; left: 0; bottom: 0; width: 100%; background: var(--cyan);
  }
  .card--front .card__band { height: 24px; }
  .card--back .card__band { height: 28px; }
</style>
</head>
<body>
<main class="canvas">

  <section class="card card--front" aria-label="Card front">
    <svg class="card__shapes" width="622" height="373" viewBox="0 0 622 373">
      <polygon points="0,0 256,0 338,349 0,349" fill="var(--ink)"/>
      <polygon points="256,0 349,0 312,85 359,279 333,326" fill="var(--cyan)"/>
      <line x1="312" y1="85" x2="290" y2="136" stroke="var(--cyan-deep)" stroke-width="3"/>
    </svg>

    <p class="brand-mini">Northgate Advisory</p>

    <div class="division">
      <div class="division__name">TRELLISWORKS</div>
      <div class="division__tagline">Practical Sector Guidance</div>
    </div>

    <svg class="contact-icons" width="622" height="373" viewBox="0 0 622 373" aria-hidden="true">
      <g fill="var(--paper)">
        <circle cx="311" cy="151" r="4.5"/>
        <path d="M303 164 q8 -10 16 0 z"/>
        <path d="M309 184 q8 -6 16 0 l-2 4 h-3 l-1 -2 h-4 l-1 2 h-3 z"/>
        <rect x="311" y="188" width="12" height="6" rx="2"/>
      </g>
      <g fill="none" stroke="var(--paper)" stroke-width="1.6">
        <rect x="319" y="212" width="14" height="9" rx="1"/>
        <path d="M319 212 l7 5 l7 -5"/>
      </g>
    </svg>

    <h1 class="holder__name">D<span class="accent">O</span>RIAN MERCADO</h1>
    <ul class="holder__details">
      <li>Managing Director</li>
      <li>+61 400 000 123</li>
      <li>dorian@northgate.example</li>
    </ul>

    <div class="card__band"></div>
  </section>

  <section class="card card--back" aria-label="Card back">
    <p class="back-brand__name">Northgate Group</p>
    <p class="back-brand__tagline">Seeing past the usual lines</p>
    <div class="card__band"></div>
  </section>

</main>
</body>
</html>
```